UPDATED Drawing Nearer: A Memoir after Divorce

I need a cover front, spine and back, for e book and print for a memoir that is for women, and perhaps some men. It is modern, about the modern world, and yet must indicate how we strive for intimacy in a modern tech age. There are laugh out loud moments, and poignant moments. It is upbeat, thoughtful, and full of characters.

We have two images in mind.

The first involves showing a woman's dress with angel wings on it, or a high heeled shoe with angel wings on it, or perhaps a pair of women's earrings with angel wings. It must indicate a woman who is modern going dating again (ie a dress), but who is thinking now about her spirituality (ie angel wings). There are lots of images out there and I have attached a few for reference. Soft colours here: feminine luxury read.

The other image I first had in mind is a friendly font, something like was used for the UK edition of Tide Under Glass by Bettina Frask, against white, with a small image of two brikko-type yellow figures, one male, one female, under a bed sheet. Or the early human computer figures of the 1980s, in a funny position suggesting a goal for relationship but the distance of computer created identikit people. You know those people they made of little yellow pixelated squares? :)

Title is Drawing Nearer

Subtitle, smaller, A Memoir after Divorce

Author name is Marla Quinlet

Press is Harrowfield Press and the logo for the spine is attached.

Thank you! Have fun :)

Target Market(s)

UK and US women (perhaps Europe) from 28-34 with some range either way. Not to exclude men. Think Swim Sing Rest audience, and A Field of Wrens audience. Both those covers might be useful. Also think of the book Slow Dials. Memoirs that have hit the bestseller lists with an honest take on love, sex, dating and Drawing Nearer. We are not looking to sexy with the small image: humorous and of a period, hence the idea for chompit style people or brikko people under the sheets.

Font styles to use
Other font styles liked:
• modern design fonts, art house fonts

Requirements
Must have
• Warmth, sophistication, humour. It's a book for readers. A simple, clear marketing on the front with the font, colour and image. Modern, not to fresh but not romantic and feminine. Think city woman on a retreat to touch the heart.
Nice to have
• A smile on looking at it. Fonts that are not too square. Some fluidity in the font to show some emotional flow. Not too stark. See other covers on my site marlaquinlet.example. (Mostly Layout Guild). This should look different again but fit the brand.

```html
<!DOCTYPE html>
<html lang="en">
<head>
<meta charset="utf-8">
<title>Drawing Nearer — Marla Quinlet</title>
<link rel="stylesheet" href="https://fonts.googleapis.com/css2?family=Petrona:wght@700&family=Jost:wght@400&display=swap">
<style>
  :root {
    --paper: #ffffff;
    --ink: #1e1e1c;
    --bed-wood: #d99a55;
    --sheet: #f4f1ee;
    --figure-yellow: #f5e400;
  }
  html, body {
    margin: 0;
    padding: 0;
    overflow: hidden;
    background: var(--paper);
  }
  .cover {
    position: relative;
    width: 769px;
    height: 1200px;
    background: var(--paper);
    color: var(--ink);
    overflow: hidden;
  }
  .title {
    position: absolute;
    top: 88px;
    left: 0;
    width: 100%;
    margin: 0;
    text-align: center;
    font-family: "Petrona", Georgia, serif;
    font-weight: 700;
    font-size: 168px;
    line-height: 162px;
    letter-spacing: -3px;
    white-space: nowrap;
  }
  .title span { display: block; }
  .bed-artwork {
    position: absolute;
    left: 240px;
    top: 620px;
    width: 322px;
    height: 148px;
  }
  .author {
    position: absolute;
    top: 875px;
    left: 0;
    width: 100%;
    margin: 0;
    text-align: center;
    font-family: "Petrona", Georgia, serif;
    font-weight: 700;
    white-space: nowrap;
    letter-spacing: -2px;
  }
  .author .first {
    display: block;
    font-size: 104px;
    line-height: 108px;
  }
  .author .last {
    display: block;
    font-size: 118px;
    line-height: 116px;
  }
  .subtitle {
    position: absolute;
    top: 1130px;
    left: 0;
    width: 100%;
    margin: 0;
    text-align: center;
    font-family: "Jost", "Futura", sans-serif;
    font-weight: 400;
    font-size: 35px;
    line-height: 44px;
    letter-spacing: 1px;
  }
</style>
</head>
<body>
  <main class="cover">
    <h1 class="title"><span>drawing</span><span>nearer</span></h1>

    <svg class="bed-artwork" viewBox="0 0 322 148" role="img"
         aria-label="Small illustration of a wooden bed with four yellow pixel-block figures peeking out from under a spotted sheet">
      <defs>
        <linearGradient id="bedTones" x1="0" y1="0" x2="0" y2="1">
          <stop offset="0" stop-color="var(--bed-wood)"/>
          <stop offset="0.3" stop-color="var(--sheet)"/>
          <stop offset="0.55" stop-color="var(--figure-yellow)" stop-opacity="0.55"/>
          <stop offset="0.75" stop-color="var(--sheet)"/>
          <stop offset="1" stop-color="var(--bed-wood)"/>
        </linearGradient>
      </defs>
      <rect x="0" y="0" width="322" height="148" rx="6" fill="url(#bedTones)"/>
    </svg>

    <p class="author"><span class="first">marla</span><span class="last">quinlet</span></p>

    <p class="subtitle">a memoir after divorce</p>
  </main>
</body>
</html>
```